Lara Joy Industries Wix Site

Company website run as a hobby by my daughter Lara. She wants to be able to offer multiple products for sale online (so etail enabled). Personalized products like bracelets and necklaces with people's names. Piggy Banks with kids names. Meadow Ranger cookies when in season. Not childish in presentation but easy to navigate by kids. Big images like on original website (larajoycookies.com). Same humor as on that site (go to the cart and empty it and you will get the idea. Colors Gold like on the bird in her attached card. Blue should be lighter than that card (robins egg type of blue). Avoid the green on the biz card. Basics of a new website with About Us, Contact, social media and a cart with payment options via paypal. mobile version nice to have but not mandataory.

```html
<!DOCTYPE html>
<html lang="en">
<head>
<meta charset="utf-8">
<title>Lara Joy Industries – Personalised Gifts</title>
<link href="https://fonts.googleapis.com/css2?family=Libre+Franklin:wght@400;500;600&family=Arimo:wght@400;700&family=Libre+Caslon+Text:wght@400&family=Mystery+Quest&display=swap" rel="stylesheet">
<style>
  :root {
    --gold: #b8952d;
    --gold-text: #b08d2a;
    --robin: #4bb8cc;
    --navy: #003e6b;
    --ink: #222222;
    --body: #666666;
    --card-grey: #f4f4f4;
    --line: #e6e6e6;
    --footer: #3b3b3b;
    --footer-head: #e2b23a;
    --search: #4a4a4a;
  }
  * { box-sizing: border-box; margin: 0; padding: 0; }
  html, body { width: 1200px; height: 2302px; overflow: hidden; background: #ffffff; }
  body { position: relative; font-family: "Arimo", Arial, sans-serif; color: var(--ink); }
  a { color: inherit; text-decoration: none; }
  ul { list-style: none; }

  /* Header */
  .site-header { position: absolute; top: 0; left: 0; width: 1200px; height: 109px; }
  .brand { position: absolute; left: 130px; top: 38px; }
  .brand-name { font-family: "Libre Franklin", sans-serif; font-weight: 500; font-size: 26px; color: var(--ink); letter-spacing: 0.2px; }
  .cart-summary { position: absolute; left: 880px; top: 36px; display: flex; align-items: center; gap: 18px; }
  .cart-icon { width: 42px; height: 42px; border-radius: 50%; border: 1px solid #e2e2e2; display: flex; align-items: center; justify-content: center; }
  .cart-title { font-family: "Libre Franklin", sans-serif; font-size: 14px; color: #333; display: block; }
  .cart-count { font-size: 12px; color: var(--robin); display: block; margin-top: 6px; }

  /* Navigation */
  .main-nav { position: absolute; top: 109px; left: 0; width: 1200px; height: 49px; background: var(--robin); }
  .nav-list { position: absolute; left: 130px; top: 0; height: 49px; display: flex; }
  .nav-list li a { display: block; height: 49px; line-height: 49px; padding: 0 37px; color: #fff; font-family: "Libre Franklin", sans-serif; font-size: 14px; font-weight: 500; }
  .nav-list li.active a { background: var(--navy); padding: 0 31px; }
  .nav-list li:nth-child(2) a { padding-left: 38px; }
  .search-btn { position: absolute; left: 1010px; top: 0; width: 60px; height: 49px; background: var(--search); display: flex; align-items: center; justify-content: center; }

  /* Hero slider */
  .hero { position: absolute; left: 130px; top: 180px; width: 940px; height: 469px; background: linear-gradient(90deg, #cd9a6b 0%, #e2b88d 45%, #e9c6a0 75%, #d7a87c 100%); overflow: hidden; }
  .hero-photo { position: absolute; left: 560px; top: 0; width: 300px; height: 469px; background: radial-gradient(ellipse at 50% 70%, #f3ece4 0%, #e8cdb0 45%, rgba(226,184,141,0) 75%); }
  .hero-copy { position: absolute; left: 89px; top: 150px; color: #fff; font-family: "Libre Franklin", sans-serif; font-size: 22px; line-height: 50px; width: 480px; }
  .hero-copy .script { font-family: "Mystery Quest", cursive; font-size: 38px; color: #1c1208; }
  .hero-arrow { position: absolute; top: 407px; }
  .hero-arrow.prev { left: 155px; }
  .hero-arrow.next { left: 1030px; }
  .hero-dots { position: absolute; left: 562px; top: 614px; display: flex; gap: 8px; }
  .hero-dots span { width: 13px; height: 13px; border-radius: 50%; background: #fff; }
  .hero-dots span.current { background: #222; }

  /* Promo boxes */
  .promos { position: absolute; left: 130px; top: 686px; width: 940px; height: 170px; display: flex; gap: 20px; }
  .promo { width: 300px; height: 170px; color: #fff; font-family: "Libre Caslon Text", serif; text-align: center; text-transform: uppercase; display: flex; flex-direction: column; justify-content: center; }
  .promo.gold { background: var(--gold); }
  .promo.robin { background: var(--robin); }
  .promo.navy { background: var(--navy); }
  .promo .small { font-size: 13px; letter-spacing: 0.3px; }
  .promo .mid { font-size: 26px; line-height: 1.2; }
  .promo .big { font-size: 56px; line-height: 1.05; }
  .promo .faint { font-size: 12px; color: #9fb4c7; }

  /* Welcome */
  .welcome { position: absolute; left: 130px; top: 920px; width: 940px; text-align: center; }
  .welcome h1 { font-family: "Libre Franklin", sans-serif; font-weight: 400; font-size: 30px; color: #222; }
  .welcome h1 span { color: var(--gold-text); }
  .welcome p { margin-top: 18px; font-size: 12.5px; line-height: 29px; color: var(--body); padding: 0 10px; }
  .btn-read { display: inline-block; margin-top: 22px; width: 132px; height: 42px; line-height: 42px; background: var(--robin); color: #fff; font-family: "Libre Franklin", sans-serif; font-size: 14px; }
  .divider { position: absolute; left: 130px; top: 1148px; width: 940px; height: 1px; background: var(--line); }

  /* Featured products */
  .featured-title { position: absolute; left: 130px; top: 1185px; width: 940px; text-align: center; font-family: "Libre Franklin", sans-serif; font-weight: 400; font-size: 29px; color: #222; }
  .featured-title span { color: var(--navy); font-weight: 500; }
  .product-grid { position: absolute; left: 130px; top: 1248px; width: 940px; display: grid; grid-template-columns: repeat(4, 220px); column-gap: 20px; row-gap: 31px; }
  .product { width: 220px; height: 328px; background: var(--card-grey); }
  .product.highlight { box-shadow: 0 2px 6px rgba(0,0,0,0.25); }
  .product-image { height: 166px; border: 1px solid #ececec; }
  .product-info { text-align: center; padding-top: 24px; }
  .product-name { font-family: "Libre Franklin", sans-serif; font-weight: 500; font-size: 16px; color: #111; }
  .product-desc { margin-top: 12px; font-size: 12px; line-height: 22px; color: var(--body); padding: 0 26px; }
  .product-buy { display: flex; align-items: center; padding: 0 18px; margin-top: 14px; }
  .price { font-family: "Libre Franklin", sans-serif; font-weight: 600; font-size: 18px; color: var(--navy); }
  .buy-cart { margin-left: auto; margin-right: 9px; }
  .btn-view { width: 61px; height: 32px; line-height: 32px; background: var(--robin); color: #fff; font-size: 13px; text-align: center; }

  /* Footer */
  .site-footer { position: absolute; left: 0; top: 2003px; width: 1200px; height: 299px; background: var(--footer); }
  .footer-col { position: absolute; top: 46px; }
  .footer-col h3 { font-family: "Libre Franklin", sans-serif; font-weight: 500; font-size: 15px; color: var(--footer-head); text-transform: uppercase; }
  .footer-col ul { margin-top: 17px; }
  .footer-col li { font-size: 12.5px; color: #eee; line-height: 29px; padding-left: 20px; position: relative; }
  .footer-col li::before { content: ""; position: absolute; left: 1px; top: 13px; width: 5px; height: 5px; border-radius: 50%; background: var(--footer-head); }
  .social { display: flex; gap: 6px; margin-top: 25px; }
  .social span { width: 30px; height: 30px; border-radius: 50%; background: #fff; }
  .copyright { margin-top: 44px; font-size: 12.5px; color: #eee; }
</style>
</head>
<body>

<header class="site-header">
  <a class="brand" href="#">
    <span class="brand-name">Lara Joy Industries</span>
  </a>
  <div class="cart-summary">
    <span class="cart-icon">
      <svg width="18" height="16" viewBox="0 0 18 16"><path d="M1 5h16l-2 9H3z" fill="none" stroke="#666" stroke-width="1.6"/><path d="M5 5l3-4M13 5l-3-4M6 8v3M9 8v3M12 8v3" stroke="#666" stroke-width="1.4"/></svg>
    </span>
    <span>
      <span class="cart-title">My Shopping Cart</span>
      <span class="cart-count">(0) Item</span>
    </span>
  </div>
</header>

<nav class="main-nav">
  <ul class="nav-list">
    <li class="active"><a href="#">Home</a></li>
    <li><a href="#">About Us</a></li>
    <li><a href="#">Services</a></li>
    <li><a href="#">Blog</a></li>
    <li><a href="#">Testimonials</a></li>
    <li><a href="#">News</a></li>
    <li><a href="#">Contact Us</a></li>
  </ul>
  <a class="search-btn" href="#" aria-label="Search">
    <svg width="22" height="22" viewBox="0 0 22 22"><circle cx="13" cy="9" r="6" fill="none" stroke="#fff" stroke-width="2"/><path d="M8.5 13.5L2 20" stroke="#fff" stroke-width="3" stroke-linecap="round"/></svg>
  </a>
</nav>

<section class="hero">
  <div class="hero-photo" role="img" aria-label="Photo of a woman in a white strapless dress wearing a pearl bracelet"></div>
  <p class="hero-copy">
    We Personalised products like<br>
    <span class="script">Bracelets &amp; Necklaces</span> with<br>
    people's names. <span class="script">Piggy Banks</span> with<br>
    kids names.
  </p>
</section>
<svg class="hero-arrow prev" width="20" height="36" viewBox="0 0 20 36"><path d="M16 4L4 18l12 14" fill="none" stroke="#fff" stroke-width="3"/></svg>
<svg class="hero-arrow next" width="20" height="36" viewBox="0 0 20 36"><path d="M4 4l12 14L4 32" fill="none" stroke="#fff" stroke-width="3"/></svg>
<div class="hero-dots"><span class="current"></span><span></span><span></span><span></span></div>

<section class="promos">
  <div class="promo gold">
    <span class="mid">Special Offer</span>
    <span class="big">10% Off</span>
    <span class="small">When you use credit card</span>
  </div>
  <div class="promo robin">
    <span class="big">Sale</span>
    <span class="small">Extra line just added</span>
    <span class="mid" style="margin-top:10px">Up to 20% off</span>
  </div>
  <div class="promo navy">
    <span class="mid">Free<br>Shipping</span>
    <span class="small" style="font-size:19px;margin-top:14px">On orders over $99</span>
    <span class="faint" style="margin-top:6px">Offer is on our store items only</span>
  </div>
</section>

<section class="welcome">
  <h1>WELCOME <span>TO OUR STORE!</span></h1>
  <p>Lorem ipsum dolor sit amet conse ctetur adipisicing elit, sed do eiusmod tempor incididunt ut labore et dolore magna aliqua. Ut enim ad minim veniam, quis nostrud exercitation ullamco laboris nisi ut aliquip ex ea commodo consequat. Duis aute irure dolor in reprehenderit in voluptate velit esse cillum dolore eu fugiat nulla pariatur. Excepteur sint occaecat cupidatat non proident, sunt in culpa.</p>
  <a class="btn-read" href="#">Read More</a>
</section>
<div class="divider"></div>

<h2 class="featured-title">Featured <span>Products</span></h2>

<section class="product-grid">
  <article class="product highlight">
    <div class="product-image" role="img" aria-label="Turquoise bead necklace" style="background:radial-gradient(circle at 50% 50%, #5cc3d6 0%, #bfe6ee 40%, #fff 70%)"></div>
    <div class="product-info"><h3 class="product-name">Product Name</h3><p class="product-desc">Excepteur sint occaecat cupid atat sunt in culpa.</p>
      <div class="product-buy"><span class="price">$29.32</span><svg class="buy-cart" width="14" height="12" viewBox="0 0 14 12"><path d="M0 1h3l2 7h7l1.5-5H4" fill="none" stroke="#333" stroke-width="1.6"/><circle cx="6" cy="10.5" r="1.2" fill="#333"/><circle cx="11" cy="10.5" r="1.2" fill="#333"/></svg><a class="btn-view" href="#">view</a></div></div>
  </article>
  <article class="product">
    <div class="product-image" role="img" aria-label="Pink piggy bank with a child's name" style="background:radial-gradient(circle at 50% 50%, #f4bccb 0%, #fbe3ea 40%, #fff 70%)"></div>
    <div class="product-info"><h3 class="product-name">Product Name</h3><p class="product-desc">Excepteur sint occaecat cupid atat sunt in culpa.</p>
      <div class="product-buy"><span class="price">$29.32</span><svg class="buy-cart" width="14" height="12" viewBox="0 0 14 12"><path d="M0 1h3l2 7h7l1.5-5H4" fill="none" stroke="#333" stroke-width="1.6"/><circle cx="6" cy="10.5" r="1.2" fill="#333"/><circle cx="11" cy="10.5" r="1.2" fill="#333"/></svg><a class="btn-view" href="#">view</a></div></div>
  </article>
  <article class="product">
    <div class="product-image" role="img" aria-label="Multicoloured glass bead necklace" style="background:radial-gradient(circle at 50% 45%, #e0b45a 0%, #d9e6c8 35%, #fff 70%)"></div>
    <div class="product-info"><h3 class="product-name">Product Name</h3><p class="product-desc">Excepteur sint occaecat cupid atat sunt in culpa.</p>
      <div class="product-buy"><span class="price">$29.32</span><svg class="buy-cart" width="14" height="12" viewBox="0 0 14 12"><path d="M0 1h3l2 7h7l1.5-5H4" fill="none" stroke="#333" stroke-width="1.6"/><circle cx="6" cy="10.5" r="1.2" fill="#333"/><circle cx="11" cy="10.5" r="1.2" fill="#333"/></svg><a class="btn-view" href="#">view</a></div></div>
  </article>
  <article class="product">
    <div class="product-image" role="img" aria-label="Black, orange and white bead necklace" style="background:radial-gradient(circle at 50% 55%, #d86a3e 0%, #eed2c4 35%, #fff 70%)"></div>
    <div class="product-info"><h3 class="product-name">Product Name</h3><p class="product-desc">Excepteur sint occaecat cupid atat sunt in culpa.</p>
      <div class="product-buy"><span class="price">$29.32</span><svg class="buy-cart" width="14" height="12" viewBox="0 0 14 12"><path d="M0 1h3l2 7h7l1.5-5H4" fill="none" stroke="#333" stroke-width="1.6"/><circle cx="6" cy="10.5" r="1.2" fill="#333"/><circle cx="11" cy="10.5" r="1.2" fill="#333"/></svg><a class="btn-view" href="#">view</a></div></div>
  </article>
  <article class="product">
    <div class="product-image" role="img" aria-label="Gold chain necklace with pink and blue gems" style="background:radial-gradient(circle at 50% 50%, #e6b4b0 0%, #f1e6dc 40%, #faf7f4 70%)"></div>
    <div class="product-info"><h3 class="product-name">Product Name</h3><p class="product-desc">Excepteur sint occaecat cupid atat sunt in culpa.</p>
      <div class="product-buy"><span class="price">$29.32</span><svg class="buy-cart" width="14" height="12" viewBox="0 0 14 12"><path d="M0 1h3l2 7h7l1.5-5H4" fill="none" stroke="#333" stroke-width="1.6"/><circle cx="6" cy="10.5" r="1.2" fill="#333"/><circle cx="11" cy="10.5" r="1.2" fill="#333"/></svg><a class="btn-view" href="#">view</a></div></div>
  </article>
  <article class="product">
    <div class="product-image" role="img" aria-label="Silver letter beads spelling love on a chain" style="background:linear-gradient(135deg, #8b7a6c 0%, #d8cfc6 45%, #efe9e3 100%)"></div>
    <div class="product-info"><h3 class="product-name">Product Name</h3><p class="product-desc">Excepteur sint occaecat cupid atat sunt in culpa.</p>
      <div class="product-buy"><span class="price">$29.32</span><svg class="buy-cart" width="14" height="12" viewBox="0 0 14 12"><path d="M0 1h3l2 7h7l1.5-5H4" fill="none" stroke="#333" stroke-width="1.6"/><circle cx="6" cy="10.5" r="1.2" fill="#333"/><circle cx="11" cy="10.5" r="1.2" fill="#333"/></svg><a class="btn-view" href="#">view</a></div></div>
  </article>
  <article class="product">
    <div class="product-image" role="img" aria-label="Coral piggy bank with a child's name" style="background:radial-gradient(circle at 50% 50%, #f08a8c 0%, #f8cfcf 40%, #fff 70%)"></div>
    <div class="product-info"><h3 class="product-name">Product Name</h3><p class="product-desc">Excepteur sint occaecat cupid atat sunt in culpa.</p>
      <div class="product-buy"><span class="price">$29.32</span><svg class="buy-cart" width="14" height="12" viewBox="0 0 14 12"><path d="M0 1h3l2 7h7l1.5-5H4" fill="none" stroke="#333" stroke-width="1.6"/><circle cx="6" cy="10.5" r="1.2" fill="#333"/><circle cx="11" cy="10.5" r="1.2" fill="#333"/></svg><a class="btn-view" href="#">view</a></div></div>
  </article>
  <article class="product">
    <div class="product-image" role="img" aria-label="Colourful charm bead bracelet" style="background:radial-gradient(circle at 50% 50%, #c98bb8 0%, #e3dcec 40%, #fff 70%)"></div>
    <div class="product-info"><h3 class="product-name">Product Name</h3><p class="product-desc">Excepteur sint occaecat cupid atat sunt in culpa.</p>
      <div class="product-buy"><span class="price">$29.32</span><svg class="buy-cart" width="14" height="12" viewBox="0 0 14 12"><path d="M0 1h3l2 7h7l1.5-5H4" fill="none" stroke="#333" stroke-width="1.6"/><circle cx="6" cy="10.5" r="1.2" fill="#333"/><circle cx="11" cy="10.5" r="1.2" fill="#333"/></svg><a class="btn-view" href="#">view</a></div></div>
  </article>
</section>

<footer class="site-footer">
  <div class="footer-col" style="left:135px">
    <h3>Information</h3>
    <ul><li>Home</li><li>Search</li><li>About us</li><li>Blog</li><li>Documentation</li><li>Contact us</li></ul>
  </div>
  <div class="footer-col" style="left:372px">
    <h3>Products</h3>
    <ul><li>Specials</li><li>New products</li><li>Top sellers</li><li>Our stores</li><li>Contact us</li><li>Pages configuration</li><li>Sitemap</li></ul>
  </div>
  <div class="footer-col" style="left:614px">
    <h3>My Account</h3>
    <ul><li>My orders</li><li>My credit slips</li><li>My addresses</li><li>My personal info</li><li>My vouchers</li></ul>
  </div>
  <div class="footer-col" style="left:854px">
    <h3>Follow Us</h3>
    <div class="social" aria-label="Social media links"><span></span><span></span><span></span><span></span><span></span></div>
    <p class="copyright">© 2014Yoursite. All Rights Reserved.</p>
  </div>
</footer>

</body>
</html>
```